Business card required for IT Consultancy Business - Tealbrook Consulting.
Company provides the whole nine yards of services across IT Architecture, design and execution.
Basically we provide consulting services to help businesses make sure their technology is enabling their business strategy.
Design for front and back required.
We would like the front of the card to inlcude:
Name
Title
Mobile number
email address
www.tbkc.com.au
Company logos attached.
Thank you
Industry/Entity Type
Business
Contact Information for Business Card
Name
Title
Mobile number
email address
www.tbkc.com.au
Look and feel
Each slider illustrates characteristics of the customer's brand and the style your logo design should communicate.

```html
<!DOCTYPE html>
<html lang="en">
<head>
<meta charset="utf-8">
<title>Tealbrook Consulting – Business Card</title>
<link rel="stylesheet" href="https://fonts.googleapis.com/css2?family=Open+Sans:wght@400;600;800&display=swap">
<style>
  :root {
    --brand-blue: #1275c0;
    --brand-orange: #f15a29;
    --card-black: #0d0d0d;
    --ink-white: #ffffff;
    --stage: #ecebea;
  }
  * { box-sizing: border-box; margin: 0; padding: 0; }
  html, body {
    width: 1200px;
    height: 900px;
    overflow: hidden;
    background: var(--stage);
    font-family: "Open Sans", Arial, sans-serif;
  }
  .canvas {
    position: relative;
    width: 1200px;
    height: 900px;
  }
  .card {
    position: absolute;
    overflow: hidden;
    box-shadow: 0 6px 18px rgba(0,0,0,0.18);
  }
  .card-front {
    left: 78px;
    top: 33px;
    width: 588px;
    height: 365px;
    background: var(--brand-blue);
    color: var(--ink-white);
  }
  .wordmark {
    position: absolute;
    left: 26px;
    top: 92px;
    display: flex;
    align-items: center;
    gap: 12px;
  }
  .wordmark-name {
    font-weight: 800;
    font-size: 40px;
    letter-spacing: 1px;
    color: var(--brand-orange);
    line-height: 1;
  }
  .wordmark-dot {
    width: 18px;
    height: 18px;
    border-radius: 50%;
    background: var(--brand-orange);
  }
  .person {
    position: absolute;
    left: 23px;
    top: 186px;
  }
  .person-name {
    font-weight: 600;
    font-size: 19px;
    line-height: 1.2;
  }
  .person-title {
    font-size: 15px;
    line-height: 1.3;
  }
  .contact-list {
    position: absolute;
    left: 24px;
    top: 278px;
    list-style: none;
  }
  .contact-item {
    display: flex;
    align-items: center;
    gap: 7px;
    font-size: 15px;
    line-height: 21px;
  }
  .contact-icon {
    width: 13px;
    height: 13px;
    fill: var(--ink-white);
  }
  .card-back {
    left: 389px;
    top: 505px;
    width: 566px;
    height: 352px;
    background: var(--card-black);
    display: flex;
    align-items: center;
    justify-content: center;
    gap: 14px;
  }
  .back-dot {
    width: 20px;
    height: 20px;
    border-radius: 50%;
    background: var(--brand-orange);
  }
  .back-name {
    font-weight: 800;
    font-size: 30px;
    letter-spacing: 1px;
    color: var(--ink-white);
  }
</style>
</head>
<body>
<main class="canvas">
  <section class="card card-front" aria-label="Card front">
    <div class="wordmark">
      <span class="wordmark-name">TEALBROOK</span>
      <span class="wordmark-dot"></span>
    </div>
    <div class="person">
      <p class="person-name">Daniel Hargreave</p>
      <p class="person-title">Managing Director</p>
    </div>
    <ul class="contact-list">
      <li class="contact-item">
        <svg class="contact-icon" viewBox="0 0 24 24" aria-hidden="true"><path d="M6.6 10.8a15.1 15.1 0 0 0 6.6 6.6l2.2-2.2a1 1 0 0 1 1-.25 11.4 11.4 0 0 0 3.6.57 1 1 0 0 1 1 1V20a1 1 0 0 1-1 1A17 17 0 0 1 3 4a1 1 0 0 1 1-1h3.5a1 1 0 0 1 1 1c0 1.25.2 2.45.57 3.57a1 1 0 0 1-.25 1z"/></svg>
        <span>0400 555 218</span>
      </li>
      <li class="contact-item">
        <svg class="contact-icon" viewBox="0 0 24 24" aria-hidden="true"><path d="M3 6h18v12H3z M3 6l9 7 9-7" stroke="#1275c0" stroke-width="1.5"/></svg>
        <span>hello@tealbrook.com.au</span>
      </li>
      <li class="contact-item">
        <svg class="contact-icon" viewBox="0 0 24 24" aria-hidden="true"><circle cx="12" cy="12" r="10"/><path d="M2 12h20M12 2c3 3 3 17 0 20M12 2c-3 3-3 17 0 20" stroke="#1275c0" stroke-width="1.3" fill="none"/></svg>
        <span>www.tbkc.com.au</span>
      </li>
    </ul>
  </section>

  <section class="card card-back" aria-label="Card back">
    <span class="back-dot"></span>
    <span class="back-name">TEALBROOK</span>
  </section>
</main>
</body>
</html>
```